interior designer/stylist looking for a letter press business card to reflect the stylish work

Hello Designers,
I need a business card design for an company called Harrow Fenwick Interior Design. I'm aiming at the high end residential and private client market in London providing sleek simple interiors. I'd like my business card to be snapboard worthy and expensive looking, i want people to clip it and for it to have a sought after look, and want prospective customers to hire me as their interior designer as my card is so beautiful.
I love letter press design. I also like the use of colour/foil on the edge.
Colour combos & general things I like -
Black and White
Navy Blue and Gold
Neutral colours (muted palette of greys whites navys beiges)
White Marble & brass
Vosque (fashion designer)
....also open to other suggestions....
Please dont take the pink in the attached photos too literally. i'd like the card to look more masculine than feminine.
I'd like Harrow Fenwick on one side in one font, with interior design underneath so one word will make the statement....... unless anyone has any other ideas, open to suggestions.
I'd like a really simple font and for the whole card to look very graphic.
my details -
Marta Quibbley
Interior Designer & Stylist
email marta@harrowfenwickinteriors.co.uk
phone +447700184396
website wwww.harrowfenwickinteriors.co.uk
GO GO GO!! EXCITED TO SEE THE OUTCOME!!
x L
High End Residential and private clients
Business
Contact Information for Business Card
Harrow Fenwick Interior Design & Styling
Marta Quibbley
phone +447700184396

```html
<!DOCTYPE html>
<html lang="en">
<head>
<meta charset="utf-8">
<title>Harrow Fenwick Interior Design &amp; Styling – Business Card</title>
<link rel="stylesheet" href="https://fonts.googleapis.com/css2?family=Poppins:wght@600&family=Roboto+Condensed:wght@400;700&display=swap">
<style>
  :root {
    --backdrop: #d9d8d4;
    --card: #ebddbf;
    --card-edge: #f3ead6;
    --glow: #fbf6ea;
    --ink: #3a3026;
    --ink-soft: #6b5d4c;
    --sub-grey: #8f8676;
    --logo-white: #ffffff;
    --web-ink: #5a4e40;
  }
  * { margin: 0; padding: 0; box-sizing: border-box; }
  html, body { width: 1200px; height: 1001px; overflow: hidden; }
  body { background: var(--backdrop); position: relative; }

  .card {
    position: absolute;
    top: 348px;
    width: 489px;
    height: 306px;
    background: var(--card);
    box-shadow: 4px 5px 0 var(--card-edge), 6px 8px 14px rgba(0,0,0,0.12);
    overflow: hidden;
  }
  .card--back { left: 88px; }
  .card--front { left: 636px; }

  .edge-glow {
    position: absolute;
    top: 0;
    bottom: 0;
    width: 140px;
  }
  .card--back .edge-glow {
    right: 0;
    background: linear-gradient(to right, var(--card), var(--glow));
  }
  .card--front .edge-glow {
    left: 0;
    background: linear-gradient(to left, var(--card), var(--glow));
  }

  .contact-block {
    position: absolute;
    right: 306px;
    text-align: right;
    font-family: "Roboto Condensed", sans-serif;
    color: var(--ink);
  }
  .contact-block--person { top: 72px; }
  .person-name { font-weight: 700; font-size: 15px; letter-spacing: 0.3px; }
  .person-role { font-size: 8.5px; margin-top: 5px; color: var(--ink-soft); }
  .contact-block--details { top: 174px; font-size: 8.5px; line-height: 16px; color: var(--ink-soft); }

  .website {
    position: absolute;
    left: 65px;
    top: 276px;
    font-family: "Roboto Condensed", sans-serif;
    font-size: 9px;
    letter-spacing: 7px;
    color: var(--web-ink);
    white-space: nowrap;
  }

  .brand {
    position: absolute;
    left: 150px;
    right: 20px;
    top: 126px;
    text-align: center;
  }
  .brand-name {
    font-family: "Poppins", sans-serif;
    font-weight: 600;
    font-size: 30px;
    letter-spacing: 0.5px;
    color: var(--logo-white);
    line-height: 1;
    white-space: nowrap;
  }
  .brand-tagline {
    font-family: "Roboto Condensed", sans-serif;
    font-size: 11px;
    letter-spacing: 0.6px;
    color: var(--sub-grey);
    margin-top: 4px;
  }
</style>
</head>
<body>

<section class="card card--back" aria-label="Card back with contact details">
  <div class="edge-glow" role="img" aria-label="Decorative light facets along the card edge"></div>

  <div class="contact-block contact-block--person">
    <p class="person-name">MARTA QUIBBLEY</p>
    <p class="person-role">Interior Designer &amp; Stylist</p>
  </div>
  <div class="contact-block contact-block--details">
    <p>marta@harrowfenwickinteriors.co.uk</p>
    <p>+447700184396</p>
  </div>
  <p class="website">www.harrowfenwickinteriors.co.uk</p>
</section>

<section class="card card--front" aria-label="Card front with brand name">
  <div class="edge-glow" role="img" aria-label="Decorative light facets along the card edge"></div>

  <div class="brand">
    <p class="brand-name">HARROW FENWICK</p>
    <p class="brand-tagline">INTERIOR DESIGN &amp; STYLING</p>
  </div>
</section>

</body>
</html>
```